Locksmith business card design

i need a business card design for a new locksmith/auto Locksmith company we cater for residental/commercial/industrial/vehicles locksmithing we provide a 24/7 emergency service we are fully insured and certified i like the idea of black with white writing i would like the final design to communicate we are very affordable compared to our competitors

Target Market(s)

everyone

Industry/Entity Type

Business

Contact Information for Business Card

Brenton's 24h Locksmiths, Owen Brenton, 27 marsh lane colby ferris pk428tw, brentons_locksmiths@quillmail.test,07724619038,www.brentonslocksmith.test

Requirements
Must have
• some sort of logo/picture

```html
<!DOCTYPE html>
<html lang="en">
<head>
<meta charset="utf-8">
<title>Brenton's 24h Locksmiths – Business Card</title>
<link rel="stylesheet" href="https://fonts.googleapis.com/css2?family=Bebas+Neue&display=swap">
<style>
  :root {
    --ink: #0b0b0b;
    --paper: #f4f4f2;
    --stage: #cfcfcf;
    --lock-grey: #a9a9a9;
    --white: #ffffff;
  }
  * { box-sizing: border-box; margin: 0; padding: 0; }
  html, body {
    width: 1200px;
    height: 875px;
    overflow: hidden;
    background: var(--stage);
  }
  .canvas {
    width: 1200px;
    height: 875px;
    display: flex;
    flex-direction: column;
    align-items: center;
    justify-content: center;
    gap: 48px;
    font-family: "Bebas Neue", "Arial Narrow", sans-serif;
  }
  .card {
    width: 640px;
    height: 366px;
    position: relative;
    overflow: hidden;
  }

  /* Front */
  .card--front {
    background: var(--ink);
    color: var(--white);
    display: flex;
    flex-direction: column;
    align-items: center;
    justify-content: center;
    gap: 30px;
  }
  .brand {
    display: flex;
    align-items: center;
    gap: 16px;
  }
  .brand__mark {
    width: 46px;
    height: 46px;
    background: var(--white);
    flex: none;
  }
  .brand__name {
    font-size: 48px;
    line-height: 1;
    letter-spacing: 1px;
    white-space: nowrap;
    color: var(--white);
  }
  .tagline {
    font-size: 34px;
    letter-spacing: 3px;
    line-height: 1;
  }

  /* Back */
  .card--back {
    background: var(--paper);
    color: var(--ink);
  }
  .band {
    position: absolute;
    top: 0; left: 0; right: 0;
    height: 142px;
    background: var(--ink);
    color: var(--white);
  }
  .band__brand {
    position: absolute;
    top: 22px;
    left: 26px;
    font-size: 30px;
    line-height: 1;
    letter-spacing: 0.5px;
  }
  .address {
    position: absolute;
    right: 24px;
    bottom: 14px;
    text-align: right;
    font-style: normal;
    font-size: 36px;
    line-height: 1.02;
    letter-spacing: 1.5px;
  }
  .contact {
    position: absolute;
    left: 26px;
    top: 156px;
    text-transform: uppercase;
    letter-spacing: 1.5px;
  }
  .contact__name {
    font-size: 56px;
    line-height: 1;
    color: var(--ink);
  }
  .contact__line {
    font-size: 30px;
    line-height: 1.12;
  }
  .decor-square {
    position: absolute;
    right: 24px;
    bottom: 24px;
    width: 96px;
    height: 96px;
    background: var(--lock-grey);
    border-radius: 10px;
  }
</style>
</head>
<body>
  <main class="canvas">
    <section class="card card--front" aria-label="Business card front">
      <div class="brand">
        <span class="brand__mark" aria-hidden="true"></span>
        <span class="brand__name">Brenton's 24h Locksmiths</span>
      </div>
      <p class="tagline">AFFORDABLE LOCKSMITHING 24/7</p>
    </section>

    <section class="card card--back" aria-label="Business card back">
      <header class="band">
        <p class="band__brand">Brenton's 24h Locksmiths</p>
        <address class="address">
          27 MARSH LANE<br>
          COLBY FERRIS | PK428TW
        </address>
      </header>
      <div class="contact">
        <p class="contact__name">Owen Brenton</p>
        <p class="contact__line">brentons_locksmiths@quillmail.test</p>
        <p class="contact__line">07724619038</p>
        <p class="contact__line">www.brentonslocksmith.test</p>
      </div>
      <span class="decor-square" aria-hidden="true"></span>
    </section>
  </main>
</body>
</html>
```